Online hair business needs a Glam Web and Logo design*

I am launching an online business selling Brazillian Hair Weave. My business name is Velora Locks and I would love a logo with a glamorous female image, maybe a silhouette, with long wavy hair and I would like the initials VL or VL somewhere in the logo on the top, bottom or as jewelry (earrings/necklace). It does not have to be a female image, but it needs to be eye-catching.

Industry/Entity Type

Hair And Beauty

Logo Text

Velora Locks

Number of Pages Required

1 page

Font styles to use
Sans Serif

Colors

Designer to choose colors to be used in the design.

Requirements
Nice to have
• I need to display the hair to sell, but would also like to display models or images with the hair installed. I also need to have FAQ's and would like to be able to add some videos.

```html
<!DOCTYPE html>
<html lang="en">
<head>
<meta charset="utf-8">
<title>Velora Locks</title>
<link href="https://fonts.googleapis.com/css2?family=Montserrat:wght@300;400;500;800&display=swap" rel="stylesheet">
<style>
:root{
  --stage:#2e2e2e;
  --page:#ffffff;
  --ink:#1c1c1c;
  --red:#ee1111;
  --dark:#333333;
  --light:#f2f2f2;
  --btn:#e6e6e6;
}
*{box-sizing:border-box;margin:0;padding:0}
html,body{width:1200px;height:1200px;overflow:hidden;background:var(--stage);font-family:"Montserrat",sans-serif;color:var(--ink)}
.page{position:absolute;left:391px;top:0;width:419px;height:1200px;background:var(--page);overflow:hidden}
.abs{position:absolute}

.hero{left:0;top:0;width:419px;height:234px;
  background:
    radial-gradient(ellipse 120px 150px at 62% 28%,rgba(120,78,58,.85) 0%,rgba(70,44,32,.6) 45%,rgba(0,0,0,0) 80%),
    radial-gradient(ellipse 90px 60px at 80% 92%,rgba(150,100,78,.8) 0%,rgba(0,0,0,0) 80%),
    linear-gradient(90deg,#0c0c0c 0%,#1a1412 35%,#2a1c16 60%,#141010 100%)}
.brand{left:20px;top:9px;display:flex;align-items:center;gap:5px;color:#fff;font-size:8px;font-weight:300}
.brand-dot{width:12px;height:12px;border-radius:50%;background:var(--red)}
.brand-init{color:var(--red);font-size:10px;line-height:1}
.nav{top:14px;left:133px;display:flex;gap:14px;font-size:6.6px;color:#ddd;letter-spacing:.2px}
.nav .active{color:var(--red);border-bottom:1px solid var(--red)}
.hero-kicker{left:108px;top:93px;color:#fff;font-size:15px;font-weight:300;letter-spacing:.5px;white-space:nowrap}
.hero-kicker span{background:var(--red);font-weight:500;padding:3px 3px 4px;margin-left:4px}
.hero-title{left:141px;top:114px;color:var(--red);font-size:22px;font-weight:800;letter-spacing:.3px}

.ship{top:250px;left:61px;font-size:8.6px;letter-spacing:.2px}
.btn{border:1px solid #222;background:var(--btn);font-size:7px;display:flex;align-items:center;justify-content:center;letter-spacing:.3px}
.btn.outline{background:#fff}
.promo{text-align:center;font-size:7.2px;line-height:13px;width:211px}
.photo-pale{
  background:
    radial-gradient(ellipse 45px 55px at 58% 48%,#e2cfc2 0%,rgba(226,207,194,0) 100%),
    radial-gradient(ellipse 95px 80px at 55% 38%,#d6d2cc 0%,#c9c4bd 45%,rgba(220,220,220,0) 100%),
    linear-gradient(135deg,#ececec 0%,#dcdcdc 50%,#efefef 100%)}

.ext-title{top:614px;left:0;width:419px;text-align:center;color:var(--red);font-size:16px;font-weight:400;letter-spacing:.5px}
.card{top:643px;width:97px;height:80px;border:1px solid #eee;background:#fff}
.card .swatch{left:9px;top:10px;width:14px;height:36px;background:linear-gradient(#3a2a22,#111);border-radius:3px}
.card .name{left:31px;top:12px;font-size:5.6px;color:#888;line-height:8px}
.card .meta{left:31px;top:37px;font-size:3.3px;color:#aaa;line-height:6px}
.card .rule{left:9px;top:63px;width:79px;height:1px;background:#bbb}
.card .go{right:9px;top:69px;font-size:3.3px;color:#999}

.hot{top:745px;left:0;width:419px;height:206px;background:var(--dark)}
.hot-photo{left:0;top:0;width:290px;height:206px;
  background:
    radial-gradient(ellipse 60px 80px at 22% 30%,rgba(214,168,140,.95) 0%,rgba(214,168,140,0) 100%),
    radial-gradient(ellipse 90px 50px at 25% 100%,rgba(200,150,120,.9) 0%,rgba(200,150,120,0) 100%),
    linear-gradient(100deg,#b98a6e 0%,#8c6650 28%,#6a5040 50%,#4a3c34 72%,var(--dark) 100%)}
.hot-text{left:221px;top:34px;color:#fff}
.hot-text .a{font-size:15px;font-weight:300}
.hot-text .b{font-size:16px;font-weight:300;margin-top:1px}
.hot-text .c{font-size:5.6px;margin-top:1px}

.news{top:951px;left:0;width:419px;height:118px;background:var(--light)}
.news-div{left:110px;top:24px;width:1px;height:65px;background:#ddd}
.news-head{left:137px;top:30px;font-size:7px;color:#777}
.news-sub{left:137px;top:42px;font-size:5px;color:#999}
.news-input{left:137px;top:56px;width:180px;height:18px;background:#111;color:#999;font-size:4.8px;font-style:italic;padding:6px 8px}
.news-btn{left:321px;top:56px;width:37px;height:18px;background:#c9c9c9;color:#fff;font-size:4.6px;display:flex;align-items:center;justify-content:center}

.foot{top:1069px;left:0;width:419px;height:28px;background:#fff}
.foot-text{left:26px;top:12px;font-size:4.3px;color:#444;letter-spacing:.1px}
.social{left:317px;top:9px;display:flex;gap:7px}
.social i{display:block;width:10px;height:10px;border-radius:50%}
.map{top:1097px;left:0;width:419px;height:103px;
  background:
    radial-gradient(ellipse 80px 50px at 45% 55%,rgba(232,180,130,.9) 0%,rgba(232,180,130,0) 100%),
    radial-gradient(ellipse 90px 60px at 85% 80%,rgba(150,200,220,.9) 0%,rgba(150,200,220,0) 100%),
    linear-gradient(110deg,#bfe0d8 0%,#e6dcb8 30%,#eed0a4 55%,#e8c9a0 75%,#c6e0ea 100%)}
</style>
</head>
<body>
<main class="page">
  <header class="abs hero" role="img" aria-label="Close-up portrait photo of a model with dark hair"></header>
  <div class="abs brand"><span class="brand-dot"></span><span><span class="brand-init">VL</span><br>Velora Locks</span></div>
  <nav class="abs nav"><span class="active">HOME</span><span>CATEGORIES</span><span>ABOUT US</span><span>SERVICES</span><span>CONTACT US</span></nav>
  <div class="abs hero-kicker">ADVANCEMENT FOR<span>SHAVING</span></div>
  <h1 class="abs hero-title">VELORA LOCKS</h1>

  <div class="abs ship">FREE SHIPPING WORLDWIDE ON ALL ORDERS</div>
  <div class="abs btn outline" style="left:300px;top:247px;width:55px;height:17px">LERN MORE</div>

  <div class="abs promo" style="left:0;top:317px">DISCOVER THE BEST PRODUCTS<br>FOR YOUR HAIR<br>Serse seradeas keruases seraseo adipisces ase<br>velitsed quia nones.</div>
  <div class="abs btn" style="left:78px;top:370px;width:70px;height:21px">ENTER SHOP</div>
  <div class="abs photo-pale" style="left:211px;top:275px;width:208px;height:162px" role="img" aria-label="Studio photo of a model with voluminous platinum curls"></div>

  <div class="abs photo-pale" style="left:0;top:437px;width:211px;height:162px" role="img" aria-label="Studio photo of a model with voluminous platinum curls"></div>
  <div class="abs promo" style="left:208px;top:479px">DISCOVER THE BEST PRODUCTS<br>FOR YOUR HAIR<br>Serse seradeas keruases seraseo adipisces ase<br>velitsed quia nones.</div>
  <div class="abs btn" style="left:274px;top:532px;width:70px;height:21px">ENTER SHOP</div>

  <h2 class="abs ext-title">EXTENSIONS FOR LONG HAIR</h2>
  <div class="abs card" style="left:56px">
    <div class="abs swatch" role="img" aria-label="Clip-in hair weft"></div>
    <div class="abs name">CLIP IN HAIR<br>EXTENSIONS</div>
    <div class="abs meta">7PCS Economy Set<br>7PCS Deluxe Set<br>12PCS Ultimate Set</div>
    <div class="abs rule"></div><div class="abs go">ENTER SHOP</div>
  </div>
  <div class="abs card" style="left:161px">
    <div class="abs swatch" role="img" aria-label="Natural hair bundle"></div>
    <div class="abs name">100% NATURAL<br>HAIR EXTENSIONS</div>
    <div class="abs meta">7PCS Economy Set<br>7PCS Deluxe Set<br>12PCS Ultimate Set</div>
    <div class="abs rule"></div><div class="abs go">ENTER SHOP</div>
  </div>
  <div class="abs card" style="left:265px">
    <div class="abs swatch" role="img" aria-label="Wavy tape-in hair"></div>
    <div class="abs name">TAPE IN HAIR<br>EXTENSIONS</div>
    <div class="abs meta">16 inches<br>18 inches<br>20 inches</div>
    <div class="abs rule"></div><div class="abs go">ENTER SHOP</div>
  </div>

  <section class="abs hot">
    <div class="abs hot-photo" role="img" aria-label="Photo of a model with long straight brown hair"></div>
    <div class="abs hot-text">
      <div class="a">HOT!</div>
      <div class="b">24&quot; HAIR EXTENSIONS</div>
      <div class="c">Veruases seraseo adipisces ase velitsed quia nonesam eiumos</div>
    </div>
    <div class="abs btn" style="left:222px;top:87px;width:68px;height:21px;border-color:#999">ENTER SHOP</div>
  </section>

  <section class="abs news">
    <svg class="abs" style="left:68px;top:24px" width="44" height="46" viewBox="0 0 44 46" aria-hidden="true">
      <g fill="none" stroke="#bbb" stroke-width="1.5" stroke-linejoin="round">
        <path d="M2 18 L30 4 L42 28 L14 42 Z" fill="#ddd"/>
        <path d="M2 18 L24 26 L30 4"/>
      </g>
    </svg>
    <div class="abs news-div"></div>
    <div class="abs news-head">NEWSLETTER</div>
    <div class="abs news-sub">Sign up to get exclusive offers from our favorite brands &amp; to be well up in the news.</div>
    <div class="abs news-input">your email address</div>
    <div class="abs news-btn">SIGN UP</div>
  </section>

  <footer class="abs foot">
    <div class="abs foot-text">HAIR EXTENSIONS IS PROUDLY POWERED BY PRESSLINE ENTRIES (RSS) AND COMMENTS (RSS) PRIVACY POLICY</div>
    <div class="abs social" aria-label="Social links">
      <i style="background:#3b5b98"></i><i style="background:#2aa3e0"></i><i style="background:#f0902a"></i><i style="background:#dd4b39"></i>
    </div>
  </footer>

  <div class="abs map" role="img" aria-label="Road map of south-east Brazil"></div>
</main>
</body>
</html>
```